VFX Company Business Card Design Project

The Ember Vale is a decentralized Visual Effects Studio servicing the television and feature film industries.
Project Brief:
Take our logo that was previously designed on Pixel Harbor and make a double sided business card.
Requirements:
- Card MUST be double sided.
- Front of card MUST have the yellow part of our logo against the dark grey background.
- Back of card is completely up to the designer.
- Back of card must include the complete company logo.
Please follow these File Preparation guidelines:
http://printmoor.example/infopage?file=filetype_en&s=PrintMoor_new&lang=en
Industry/Entity Type
Business
Look and feel
Each slider illustrates characteristics of the customer's brand and the style your logo design should communicate.

```html
<!DOCTYPE html>
<html lang="en">
<head>
<meta charset="utf-8">
<title>The Ember Vale – Business Card</title>
<link rel="stylesheet" href="https://fonts.googleapis.com/css2?family=Ubuntu:wght@400;500&display=swap">
<style>
  :root {
    --backdrop: #d4d4d4;
    --card: #3a3a3a;
    --accent: #f2c62a;
    --ink: #f1f1f1;
    --ink-soft: #d9d9d9;
  }
  * { box-sizing: border-box; margin: 0; padding: 0; }
  html, body { width: 1200px; height: 747px; overflow: hidden; }
  body {
    background: var(--backdrop);
    font-family: "Ubuntu", sans-serif;
    position: relative;
  }
  .card {
    position: absolute;
    top: 93px;
    width: 320px;
    height: 560px;
    background: var(--card);
    box-shadow: 0 6px 18px rgba(0,0,0,0.25);
    overflow: hidden;
  }
  .card--front { left: 230px; }
  .card--back { left: 650px; }

  /* front: brand name set vertically */
  .front-brand {
    position: absolute;
    left: 50%;
    top: 50%;
    transform: translate(-50%, -50%) rotate(-90deg);
    display: flex;
    align-items: center;
    gap: 18px;
    white-space: nowrap;
  }
  .front-brand__dot {
    width: 26px; height: 26px;
    border-radius: 50%;
    background: var(--accent);
  }
  .front-brand__name {
    color: var(--accent);
    font-weight: 500;
    font-size: 40px;
    letter-spacing: 1px;
  }

  /* back: details */
  .back-brand {
    position: absolute;
    top: 62px; left: 0; right: 0;
    text-align: center;
    color: var(--accent);
    font-weight: 500;
    font-size: 32px;
    letter-spacing: 1px;
  }
  .person {
    position: absolute;
    top: 182px; left: 36px;
  }
  .person__name {
    color: var(--accent);
    font-size: 24px;
    font-weight: 400;
    letter-spacing: 1px;
  }
  .person__role {
    color: var(--ink-soft);
    font-size: 15px;
    margin-top: 3px;
  }
  .rule {
    position: absolute;
    left: 36px; right: 0;
    height: 2px;
    background: var(--accent);
  }
  .rule--upper { top: 262px; }
  .rule--lower { top: 395px; }
  .contacts {
    position: absolute;
    top: 285px; left: 18px;
    list-style: none;
  }
  .contacts li {
    display: flex;
    align-items: baseline;
    font-size: 17px;
    line-height: 27px;
    color: var(--ink);
  }
  .contacts__key {
    width: 26px;
    color: var(--accent);
    font-size: 14px;
    text-align: center;
    margin-right: 10px;
  }
  .address {
    position: absolute;
    top: 420px; left: 36px;
    color: var(--ink);
    font-size: 17px;
    line-height: 26px;
    font-style: normal;
  }
</style>
</head>
<body>
  <section class="card card--front" aria-label="Card front">
    <div class="front-brand">
      <span class="front-brand__dot"></span>
      <span class="front-brand__name">The Ember Vale</span>
    </div>
  </section>

  <section class="card card--back" aria-label="Card back">
    <div class="back-brand">The Ember Vale</div>
    <div class="person">
      <h1 class="person__name">JOHN DOE</h1>
      <p class="person__role">Managing Partner</p>
    </div>
    <div class="rule rule--upper"></div>
    <ul class="contacts">
      <li><span class="contacts__key">t</span>(480) 555-0142</li>
      <li><span class="contacts__key">e</span>name@embervale.example</li>
      <li><span class="contacts__key">w</span>www.embervale.example</li>
    </ul>
    <div class="rule rule--lower"></div>
    <address class="address">
      1234 North Harrow Road,<br>
      Suite 1234, Alder Bay,<br>
      Region 88888
    </address>
  </section>
</body>
</html>
```